Vintrel.com- International Goal Achievement Coach Needs Website Design

I need a web design for my new company called Vintrel. I help people who are stuck, people who have a big dream, but don't know how to get there. I help them to break their dreams down into small, manageable steps... and then I'm the "kick in the shin" to get them moving and thriving!

We can all be better- We can all DO better. I inspire people to Ride Onward in the direction of your dreams.

I have uploaded my logo along with some vintage champagne posters. Please use the vintage posters as inspiration. I like the bold, vintage look and feel. I would love the main colors of the design to be black, white and metallic gold. And to follow along this vintage look and feel. Please feel free to use the logo in black or metallic gold or white.

Target Market(s)

websites that I like- janetrulsby.com & hollyp.tv

I would like to also use the vintage champagne photos attached as inspiration as well.

Industry/Entity Type

It Company

Requirements
Must have
• Tabs should include: About, Work With Me, Praise, Giving Back

On the homepage add:
* Sign up for newsletter with space to enter name and email (No click throughs)
* Upcoming Events/Sessions
* Newsletter Posts
* Resources
* Praise Section

* Large photo on top with additional photos throughout the page/site.
Nice to have
• Any additions you can bring to the table would be greatly appreciated.

```html
<!DOCTYPE html>
<html lang="en">
<head>
<meta charset="utf-8">
<title>Vintrel</title>
<link href="https://fonts.googleapis.com/css2?family=Source+Sans+3:wght@300;400;600&display=swap" rel="stylesheet">
<style>
:root{
  --slate:#2f3b48;
  --ink:#0f1317;
  --gold:#a97c50;
  --gold-light:#c49a6c;
  --gold-text:#b07d4f;
  --tan:#cfae88;
  --footer:#1b2026;
  --field:#4d545c;
  --white:#ffffff;
  --body:#222222;
}
*{margin:0;padding:0;box-sizing:border-box}
html,body{width:816px;height:1200px;overflow:hidden}
body{position:relative;background:var(--white);font-family:"Source Sans 3",Arial,sans-serif;color:var(--body)}
.abs{position:absolute}
.masthead{left:0;top:0;width:816px;height:466px;background:var(--slate)}
.brand{display:flex;align-items:center;gap:10px}
.brand-dot{width:46px;height:46px;border-radius:50%;background:var(--gold)}
.brand-name{font-size:26px;font-weight:300;color:var(--gold-light)}
.nav{right:42px;top:32px;display:flex;gap:18px;font-size:16px;font-weight:300;color:var(--white)}
.nav .active{color:var(--gold-light)}
.nav-tab{left:472px;top:0;width:38px;height:7px;background:var(--gold)}
.photo{background:linear-gradient(135deg,#b79c80,#6e5a4a)}
.hero-copy{left:375px;top:107px;width:407px;height:227px;background:var(--ink);color:var(--white)}
.hero-title{position:absolute;left:39px;top:56px;font-size:37px;font-weight:300;line-height:46px}
.hero-sub{position:absolute;left:42px;top:158px;font-size:10.5px;font-weight:400}
.about{left:375px;top:334px;width:407px;height:132px;background:var(--gold);color:var(--white)}
.about h2{position:absolute;left:27px;top:20px;font-size:16px;font-weight:400}
.about p{position:absolute;left:27px;top:46px;width:360px;font-size:8.2px;line-height:13px}
.read-more{position:absolute;right:0;bottom:0;width:71px;height:20px;background:var(--tan);color:var(--ink);font-size:9.5px;line-height:20px;text-align:center}
.card h3{font-size:15.5px;font-weight:300;color:var(--gold-text);margin-bottom:12px}
.card .pic{position:relative;width:184px;height:105px}
.card .more{position:absolute;right:-3px;bottom:4px;width:42px;height:13px;background:var(--gold);color:var(--white);font-size:8.5px;line-height:13px;text-align:center}
.card p{margin-top:12px;width:184px;font-size:8.3px;line-height:11.5px;color:var(--body)}
.feature-pic{left:480px;top:516px;width:302px;height:201px;background:linear-gradient(160deg,#9cae5a,#5a6f3a 55%,#3e4d66)}
.feature-copy{left:480px;top:717px;width:302px;height:225px;background:linear-gradient(170deg,#d9b46a 0%,#b7a183 35%,#6e6a78 75%,#5d6a3a 100%)}
.feature-copy h2{position:absolute;left:26px;top:24px;width:270px;font-size:25px;font-weight:300;line-height:31px;color:var(--ink)}
.feature-copy p{position:absolute;left:29px;top:130px;width:245px;font-size:8.3px;line-height:11.5px;color:var(--ink)}
.footer{left:0;top:996px;width:816px;height:204px;background:var(--footer);color:var(--white)}
.footer .rule{position:absolute;left:40px;top:78px;width:162px;height:1px;background:#3a4048}
.address{position:absolute;left:42px;top:85px;font-size:11.5px;line-height:18px}
.socials{position:absolute;left:42px;top:146px;display:flex;gap:6px}
.socials span{width:19px;height:19px;border-radius:50%}
.foot-nav{position:absolute;left:254px;top:17px;list-style:none;font-size:11.5px}
.foot-nav li{width:120px;height:19px;line-height:19px;padding-left:12px;margin-bottom:6px;color:var(--gold-light);font-weight:300}
.foot-nav li.active{background:var(--field);color:var(--white);border-left:3px solid var(--gold);padding-left:9px}
.signup{position:absolute;left:466px;top:20px}
.signup h2{font-size:15px;font-weight:300;color:#d5d8dc;margin-bottom:15px}
.field{width:211px;height:25px;background:var(--field);color:#a9aeb4;font-size:11px;line-height:25px;padding-left:10px;margin-bottom:9px}
.subscribe{width:95px;height:25px;background:var(--gold);color:var(--white);font-size:11.5px;line-height:25px;text-align:center;margin-top:4px}
.legal{position:absolute;top:185px;font-size:10px;color:#b9bec4}
</style>
</head>
<body>
<header class="abs masthead">
  <div class="abs nav-tab"></div>
  <div class="abs brand" style="left:35px;top:20px">
    <span class="brand-dot"></span><span class="brand-name">Vintrel</span>
  </div>
  <nav class="abs nav">
    <span class="active">About</span><span>Work With Me</span><span>Praise</span><span>Giving Back</span>
  </nav>
  <div class="abs photo" role="img" aria-label="Group of cheerful young people giving thumbs up" style="left:35px;top:107px;width:340px;height:227px;background:linear-gradient(135deg,#c9b9a6,#7a5e4c 60%,#3d4556)"></div>
  <section class="abs hero-copy">
    <h1 class="hero-title">BECOME THE happiest<br>PERSON YOU KNOW</h1>
    <p class="hero-sub">SIGN UP FOR MARA'S NEW GUIDED MEDITATIONS AND VLOG. Its Free</p>
  </section>
  <div class="abs photo" role="img" aria-label="Smiling business team standing together" style="left:35px;top:334px;width:340px;height:132px;background:linear-gradient(135deg,#e8e6e2,#b3a89c 50%,#5d5a5a)"></div>
  <section class="abs about">
    <h2>ABOUT VINTREL</h2>
    <p>Lorem Ipsum is simply dummy text of the printing and typesetting industry. Lorem Ipsum has been the industry's standard dummy text ever since the 1500s, when an unknown printer took a galley of type and Lorem Ipsum is simply dummy text of the printing and typesetting industry. Lorem Ipsum has been the industry's standard dummy text ever since the 1500s, when an unknown printer took a galley of type.</p>
    <span class="read-more">READ MORE</span>
  </section>
</header>

<article class="abs card" style="left:34px;top:484px">
  <h3>Upcoming Events/Sessions</h3>
  <div class="pic" role="img" aria-label="Man raising arms in a sunny field" style="background:linear-gradient(135deg,#e6c48c,#a88a5e 60%,#7a8a9a)"><span class="more">more</span></div>
  <p>Lorem Ipsum is simply dummy text of the printing and typesetting industry. Lorem Ipsum has been the industry's standard dummy text ever since the 1500s, when an unknown printer took a galley of type and scrambled it to make a type specimen book. It has survived</p>
</article>
<article class="abs card" style="left:255px;top:484px">
  <h3>Resources</h3>
  <div class="pic" role="img" aria-label="Mother and child in winter hats laughing" style="background:linear-gradient(135deg,#2f8a88,#c89a86 50%,#b8323a)"><span class="more">more</span></div>
  <p>Lorem Ipsum is simply dummy text of the printing and typesetting industry. Lorem Ipsum has been the industry's standard dummy text ever since the 1500s, when an unknown printer took a galley of type and scrambled it to make a type specimen book. It has survived</p>
</article>
<article class="abs card" style="left:34px;top:728px">
  <h3>Newsletter Posts</h3>
  <div class="pic" role="img" aria-label="Business team smiling together" style="background:linear-gradient(135deg,#e8e6e2,#b3a89c 50%,#5d5a5a)"><span class="more">more</span></div>
  <p>Lorem Ipsum is simply dummy text of the printing and typesetting industry. Lorem Ipsum has been the industry's standard dummy text ever since the 1500s, when an unknown printer took a galley of type and scrambled it to make a type specimen book. It has survived</p>
</article>
<article class="abs card" style="left:255px;top:728px">
  <h3>Praise Section</h3>
  <div class="pic" role="img" aria-label="Woman enjoying the sun outdoors" style="background:linear-gradient(135deg,#c9d2c2,#e8d6c2 55%,#8a5a44)"><span class="more">more</span></div>
  <p>Lorem Ipsum is simply dummy text of the printing and typesetting industry. Lorem Ipsum has been the industry's standard dummy text ever since the 1500s, when an unknown printer took a galley of type and scrambled it to make a type specimen book. It has survived</p>
</article>

<div class="abs feature-pic" role="img" aria-label="Woman with laptop relaxing in a garden chair"></div>
<section class="abs feature-copy">
  <h2>Contrary to popular belief, Lorem Ipsum is not simply random text</h2>
  <p>Lorem Ipsum is simply dummy text of the printing and typesetting industry. Lorem Ipsum has been the industry's standard dummy text ever since the 1500s, when an unknown printer took a galley of type and scrambled it to make a type specimen book. It has survived</p>
</section>

<footer class="abs footer">
  <div class="abs brand" style="left:40px;top:19px">
    <span class="brand-dot"></span><span class="brand-name">Vintrel</span>
  </div>
  <div class="rule"></div>
  <address class="address" style="font-style:normal">42 Linden Ct Marlow,<br>OR 97302 555-014-2270<br>name@vintrel.com</address>
  <div class="socials">
    <span style="background:#1da1d6"></span><span style="background:#3b5998"></span><span style="background:#0a77b5"></span><span style="background:#d9402c"></span>
  </div>
  <ul class="foot-nav">
    <li class="active">About</li><li>Work With Me</li><li>Praise</li><li>Giving Back</li><li>Contact Us</li>
  </ul>
  <form class="signup">
    <h2>Email News Letter</h2>
    <div class="field">Enter your name</div>
    <div class="field">Enter your Email</div>
    <div class="subscribe">Subscribe</div>
  </form>
  <span class="legal" style="left:40px">© 2014 vintrel.com</span>
  <span class="legal" style="right:41px">Privacy Policy</span>
</footer>
</body>
</html>
```